Childcare Centre trifold brochure

Design a contemporary trifold brochure for a childcare centre that meets Australian printing requirements with supplied content, logo's, fonts and photo's. Please refer to the attached DL flyer front and back for similar possible style and content.

Target Market(s)

Families

Industry/Entity Type

Childcare

Requirements
Must have
• refer attached content, photo's, logo's and examples. Colours should be same as Pantone purple and green and or variations of. Refer attached dl flyer example.

```html
<!DOCTYPE html>
<html lang="en">
<head>
<meta charset="utf-8">
<title>Bright Sprouts – Trifold Brochure</title>
<link rel="stylesheet" href="https://fonts.googleapis.com/css2?family=Open+Sans:wght@400;600;700&family=Cabin:wght@600;700&display=swap">
<style>
  :root {
    --purple: #8f2b8c;
    --purple-light: #a5449f;
    --purple-deep: #6d1a6a;
    --green: #33a845;
    --green-light: #4cbf55;
    --white: #ffffff;
    --paper: #ebe6e0;
    --photo-kids: #d9a9a0;
    --photo-yard: #a89a86;
    --photo-garden: #7f7663;
    --photo-child: #5e6a55;
  }
  * { box-sizing: border-box; margin: 0; padding: 0; }
  html, body { width: 1200px; height: 867px; overflow: hidden; }
  body { background: var(--paper); font-family: "Open Sans", sans-serif; color: var(--white); }

  .brochure {
    position: absolute; left: 30px; top: 30px;
    width: 1140px; height: 806px;
    display: flex; box-shadow: 0 4px 18px rgba(0,0,0,.18);
  }
  .panel { position: relative; width: 380px; height: 806px; overflow: hidden; }
  .panel-art { position: absolute; inset: 0; }

  /* Left panel */
  .panel--story { background: linear-gradient(170deg, var(--purple-light), var(--purple)); }
  .story-text {
    position: absolute; left: 30px; top: 40px; width: 322px;
    font-size: 13.5px; line-height: 1.5;
  }
  .story-text p + p { margin-top: 14px; }
  .story-text strong { font-size: 16px; font-weight: 700; }

  /* Middle panel */
  .panel--info { background: linear-gradient(180deg, var(--purple-light), var(--purple)); }
  .quotes { position: absolute; left: 26px; top: 32px; width: 330px; list-style: none; }
  .quotes li {
    position: relative; padding-left: 22px; font-size: 12.5px; line-height: 1.45;
    font-weight: 600; margin-bottom: 14px;
  }
  .quotes li::before {
    content: ""; position: absolute; left: 0; top: 4px; width: 10px; height: 10px;
    border-radius: 50%; border: 2px solid var(--green-light);
  }
  .contact-block {
    position: absolute; left: 0; top: 470px; width: 380px; text-align: center;
    font-family: "Cabin", sans-serif;
  }
  .contact-block h3 { font-size: 17px; font-weight: 700; }
  .contact-block .hours { font-family: "Open Sans", sans-serif; font-size: 13px; margin-bottom: 14px; }
  .contact-block .line { font-size: 17px; font-weight: 700; line-height: 1.35; }
  .contact-block .gap { margin-top: 12px; }
  .social {
    margin-top: 12px; display: flex; justify-content: center; align-items: center; gap: 8px;
    font-family: "Open Sans", sans-serif; font-size: 11px; letter-spacing: 1px; text-transform: uppercase;
  }
  .social .dot { width: 14px; height: 14px; border-radius: 50%; background: var(--white); opacity: .85; }

  /* Right panel */
  .panel--cover { background: var(--white); }
  .brand {
    position: absolute; left: 0; top: 26px; width: 380px; text-align: center;
    font-family: "Cabin", sans-serif;
  }
  .brand-name { display: inline-flex; align-items: center; gap: 8px; font-size: 32px; font-weight: 700; color: var(--green); }
  .brand-name .mark { width: 22px; height: 22px; border-radius: 50%; background: var(--purple); }
  .brand-tagline { font-size: 13px; font-weight: 600; color: var(--purple); margin-top: 2px; }

  .award {
    position: absolute; width: 150px; height: 150px; border-radius: 50%;
    background: var(--purple); border: 5px solid var(--white);
    display: flex; align-items: center; justify-content: center; text-align: center;
    font-family: "Cabin", sans-serif; font-weight: 700; font-size: 15px; line-height: 1.25; padding: 16px;
    box-shadow: 0 2px 6px rgba(0,0,0,.2);
  }
  .award--service { left: 22px; top: 290px; width: 160px; height: 160px; }
  .award--winner { left: 198px; top: 250px; }
  .award--finalist { left: 190px; top: 410px; width: 142px; height: 142px; }
  .rating-badge {
    position: absolute; left: 268px; top: 540px; width: 106px; height: 106px; border-radius: 50%;
    background: var(--white); display: flex; align-items: center; justify-content: center;
  }
  .rating-badge span { width: 46px; height: 46px; background: var(--green); }

  .cover-footer { position: absolute; left: 0; top: 676px; width: 380px; text-align: center; font-family: "Cabin", sans-serif; }
  .cover-footer .motto { color: var(--purple); font-size: 14px; font-weight: 700; text-transform: uppercase; line-height: 1.2; margin-bottom: 6px; }
  .cover-footer .line { font-size: 15.5px; font-weight: 700; line-height: 1.3; }
</style>
</head>
<body>
<main class="brochure">

  <!-- Panel 1: story -->
  <section class="panel panel--story">
    <svg class="panel-art" viewBox="0 0 380 806" aria-hidden="true">
      <path d="M0 430 C120 420 260 400 380 360 L380 806 L0 806 Z" fill="var(--green)"/>
      <path d="M0 440 C120 432 260 414 380 378 L380 806 L0 806 Z" fill="var(--white)"/>
      <path d="M0 448 C120 442 260 426 380 392 L380 806 L0 806 Z" fill="var(--purple-deep)"/>
      <g role="img" aria-label="Photo: children in hats and jackets exploring an outdoor garden path">
        <path d="M0 460 C130 455 250 440 345 412 C320 560 280 700 300 806 L0 806 Z" fill="var(--photo-garden)"/>
      </g>
    </svg>
    <div class="story-text">
      <p><strong>Since 2015,</strong> throughout each school term our educators run free lessons for all ages in the following: yoga, meditation, sign language, Spanish, German, Malaysian, Sri Lankan Culture, Sustainability, Noongar Culture &amp; Sport.</p>
      <p>The sign language is a particular hit with the mothers as the babies are able to sign to their parents when they are hungry or need to go to the toilet before they even start talking.</p>
      <p>The first five years of a child's development are the most crucial with 90% of their brain synapsis being formed by this time.</p>
      <p>Becoming multilingual or being able to sign has an expediential effect on the children's development outcomes which is why we offer such a vast array of authentic leaning experiences.</p>
    </div>
  </section>

  <!-- Panel 2: info -->
  <section class="panel panel--info">
    <svg class="panel-art" viewBox="0 0 380 806" aria-hidden="true">
      <path d="M0 0 L22 0 C10 120 14 280 40 380 C60 460 30 560 0 600 Z" fill="var(--purple-deep)" opacity=".35"/>
      <path d="M0 720 C120 730 260 720 380 650 L380 662 C260 734 120 744 0 736 Z" fill="var(--green)"/>
      <path d="M0 740 C120 748 260 738 380 668 L380 806 L0 806 Z" fill="var(--purple-deep)" opacity=".45"/>
      <path d="M300 806 C330 760 360 720 380 700 L380 806 Z" fill="var(--green)"/>
      <circle cx="190" cy="345" r="86" fill="var(--white)"/>
      <g role="img" aria-label="Photo: young child in a sun hat playing outdoors">
        <circle cx="190" cy="345" r="80" fill="var(--photo-child)"/>
      </g>
    </svg>
    <ul class="quotes">
      <li>"providing outdoor opportunities for learning is a critical priority for parents, teachers and the wider community"</li>
      <li>"outdoor learning was added to the Australian Curriculum in 2015, however just 34% of teachers surveyed taught outdoors for 15 minutes or more"</li>
      <li>"Nature ignites passion, inspiration, creativity &amp; purpose and plays an important role in the cognitive, emotional and physical development of children"</li>
    </ul>
    <div class="contact-block">
      <h3>Opening Hours</h3>
      <p class="hours">6:00am – 6:00pm Monday – Friday (except public holidays)</p>
      <p class="line">Address: 18 Wattle Lane,</p>
      <p class="line">Greenhill, WA 6000</p>
      <p class="line gap">Web: brightsprouts.com.au</p>
      <p class="line">Tel: 08 9000 1234</p>
      <p class="line">hello@brightsprouts.com.au</p>
      <div class="social"><span class="dot"></span>brightsproutsoz</div>
    </div>
  </section>

  <!-- Panel 3: cover -->
  <section class="panel panel--cover">
    <svg class="panel-art" viewBox="0 0 380 806" aria-hidden="true">
      <g role="img" aria-label="Photo: outdoor playground with a tree and play area">
        <rect x="0" y="230" width="380" height="420" fill="var(--photo-yard)"/>
      </g>
      <path d="M0 110 L380 110 L380 250 C300 250 200 270 110 300 C60 318 20 330 0 336 Z" fill="var(--green)"/>
      <g role="img" aria-label="Photo: group of smiling preschool children at a craft table">
        <path d="M0 120 L380 120 L380 236 C300 238 200 256 110 286 C60 302 20 314 0 318 Z" fill="var(--photo-kids)"/>
      </g>
      <path d="M0 0 L36 0 C20 80 20 200 0 340 Z" fill="var(--purple)"/>
      <path d="M0 620 C140 640 260 620 380 600 L380 806 L0 806 Z" fill="var(--green)"/>
      <path d="M0 700 C60 690 90 720 110 806 L0 806 Z" fill="var(--green-light)"/>
    </svg>
    <div class="brand">
      <div class="brand-name"><span class="mark"></span>Bright Sprouts</div>
      <p class="brand-tagline">Early Development &amp; Education Centre</p>
    </div>
    <div class="award award--service">Finalist, Early Childhood Service of the Year, 2018, 2017 &amp; 2016</div>
    <div class="award award--winner">WA State winner, Early Childhood Director of the Year 2018</div>
    <div class="award award--finalist">Finalist, Early Childhood Director of the Year, 2016</div>
    <div class="rating-badge" role="img" aria-label="Quality rating badge"><span></span></div>
    <div class="cover-footer">
      <p class="motto">Guiding the<br>stewards of the<br>future</p>
      <p class="line">Web: brightsprouts.com.au</p>
      <p class="line">Tel: 08 9000 1234</p>
      <p class="line">hello@brightsprouts.com.au</p>
    </div>
  </section>

</main>
</body>
</html>
```